Company Business Card, for Harborveldt.com Floating homes and Marinas

To design a new great looking business card that follows some how the theme of our business and website. Harborveldt.com

I have attached our logo and a copy of our existing card (boring)

   We appreciate everyones efforts so far there are some very interesting designs. We are thinking that our company is more than just a Marina manufacturer, we build many different floating products and we would like our card to show case those products. There has been one card that has done this, and we are leaning towards that design. We prefer that our logo and company name are proportional on the card, and our mission statement be also shown. Thank you                                

                                   

 We do like your designs, on the back of the card  we want to show all 6 different product types as shown on the front of our website.

                                   

Sorry some designers have the images on the front, and that is okay as well. We just want on the card all 6 areas that we manufacture.

• Must have a new look, maybe nautical, following the theme of what our company manufactures.

Logo
Company name: Consolidated Pontoon Dockworks Group, Inc.

Website: www.HarborVeldt.com

Employee name & title

Mission statement: "Craftsmanship is the keel that carries every voyage"

Our Address: 4718 Quillan Avenue, Delta, B.C. Canada, V3K 2R7

• Colour and unique presentation,

```html
<!DOCTYPE html>
<html lang="en">
<head>
<meta charset="utf-8">
<title>Consolidated Pontoon Dockworks Group — Business Card</title>
<link rel="stylesheet" href="https://fonts.googleapis.com/css2?family=Didact+Gothic&family=Montserrat:wght@700&display=swap">
<style>
  :root {
    --backdrop: #d9d9d9;
    --card: #f7f7f5;
    --ink: #2b2b2b;
    --charcoal: #262626;
    --red: #c4161c;
    --band: #1f1f1f;
    --water: #5b7184;
    --sky: #a9b9c6;
    --timber: #8a6a4c;
    --hull: #d4d6d2;
    --canopy: #5f7a5a;
  }
  * { box-sizing: border-box; margin: 0; padding: 0; }
  html, body { width: 1200px; height: 851px; overflow: hidden; }
  body {
    background: var(--backdrop);
    font-family: "Didact Gothic", "Century Gothic", sans-serif;
    color: var(--ink);
    position: relative;
  }
  .card {
    position: absolute;
    top: 271px;
    width: 540px;
    height: 309px;
    background: var(--card);
    overflow: hidden;
    box-shadow: 0 2px 8px rgba(0,0,0,.12);
  }
  .card--front { left: 40px; }
  .card--back { left: 620px; background: #fff; }

  /* front */
  .brand {
    position: absolute;
    left: 40px; top: 38px;
    display: flex; align-items: center; gap: 22px;
  }
  .brand__square {
    width: 118px; height: 88px;
    border: 3px solid var(--red);
  }
  .brand__name {
    font-size: 20px;
    line-height: 1.08;
    letter-spacing: .5px;
    text-transform: uppercase;
    color: var(--ink);
    width: 260px;
  }
  .person {
    position: absolute;
    left: 104px; top: 168px;
    text-align: left;
  }
  .person__name {
    font-family: "Montserrat", sans-serif;
    font-weight: 700;
    font-size: 14px;
    letter-spacing: .6px;
    text-transform: uppercase;
    color: var(--charcoal);
  }
  .person__title { font-size: 13px; color: var(--red); margin-top: 1px; }
  .contact {
    position: absolute;
    left: 320px; top: 170px;
    font-size: 12.5px;
    line-height: 1.3;
    color: var(--ink);
  }
  .contact__label { color: var(--red); font-family: "Montserrat", sans-serif; font-weight: 700; font-size: 11px; }
  .card__stripe {
    position: absolute; bottom: 18px; height: 14px;
  }
  .card__stripe--dark { left: 0; width: 232px; background: var(--charcoal); }
  .card__stripe--red { left: 236px; right: 0; background: var(--red); }

  /* back */
  .gallery {
    position: absolute; inset: 0;
    display: grid;
    grid-template-columns: repeat(3, 1fr);
    grid-template-rows: 1fr 34px 1fr;
    gap: 3px;
    background: #fff;
  }
  .photo { display: block; }
  .photo--marina { background: linear-gradient(180deg, var(--sky) 0%, #8c9ba6 45%, var(--water) 100%); }
  .photo--bridge { background: linear-gradient(180deg, #9fb2c4 0%, #b9c1c6 50%, #6d7f8c 100%); }
  .photo--shelter { background: linear-gradient(180deg, #dfe4e6 0%, var(--canopy) 55%, #b9a47c 100%); }
  .photo--residence { background: linear-gradient(180deg, #3e4b56 0%, #6a7b6c 55%, #2e3a44 100%); }
  .photo--houseboat { background: linear-gradient(180deg, #c8d4de 0%, var(--timber) 55%, var(--water) 100%); }
  .photo--boathouse { background: linear-gradient(180deg, #8ea0b0 0%, var(--hull) 50%, #3f5263 100%); }
  .tagline {
    grid-column: 1 / -1;
    background: var(--band);
    color: var(--red);
    font-family: "Montserrat", sans-serif;
    font-weight: 700;
    font-size: 12.5px;
    letter-spacing: .8px;
    text-transform: uppercase;
    display: flex; align-items: center; justify-content: center;
  }
</style>
</head>
<body>
  <section class="card card--front" aria-label="Business card front">
    <div class="brand">
      <div class="brand__square"></div>
      <div class="brand__name">Consolidated Pontoon Dockworks Group, Inc.</div>
    </div>
    <div class="person">
      <div class="person__name">Dorian Keswick</div>
      <div class="person__title">Senior Project Manager</div>
    </div>
    <address class="contact" style="font-style:normal">
      <div>4718 Quillan Avenue, Delta</div>
      <div>B.C. Canada, V3K 2R7</div>
      <div><span class="contact__label">T:</span> 604.555.0182</div>
      <div><span class="contact__label">E:</span> dorian@HarborVeldt.com</div>
    </address>
    <div class="card__stripe card__stripe--dark"></div>
    <div class="card__stripe card__stripe--red"></div>
  </section>

  <section class="card card--back" aria-label="Business card back">
    <div class="gallery">
      <div class="photo photo--marina" role="img" aria-label="Photo of a floating marina with docked boats"></div>
      <div class="photo photo--bridge" role="img" aria-label="Photo of a floating walkway and bridge over water"></div>
      <div class="photo photo--shelter" role="img" aria-label="Photo of a green floating boat shelter"></div>
      <div class="tagline">Craftsmanship is the keel that carries every voyage</div>
      <div class="photo photo--residence" role="img" aria-label="Photo of a modern floating home at dusk"></div>
      <div class="photo photo--houseboat" role="img" aria-label="Photo of a wooden two-storey floating house"></div>
      <div class="photo photo--boathouse" role="img" aria-label="Photo of a yacht beside a covered floating boathouse"></div>
    </div>
  </section>
</body>
</html>
```